Création d'un modèle de compte-rendus
Besoins
Cabinet de recrutement et de conseil en Ressources Humaines, nous intervenons depuis plus de 60 ans auprès d’entreprises afin de pourvoir leurs besoins en recrutement.
Nous intervenons sur tout type de postes, du cadre dirigeant à l’ouvrier, avec une majorité de postes à responsabilités.
Dans le cadre de nos recrutements, nous envoyons à l’entreprise cliente un document de synthèse des candidats intéressants que nous rencontrons. Dans ce document, nous présentons son parcours professionnel, ses informations générales (mobilité, préavis, rémunération…), ses principaux traits de personnalité, son potentiel intellectuel ainsi qu’une conclusion présentant les points forts, les axes de progrès et notre avis sur ce candidat.
Nos synthèses actuelles sont sous la forme d’un document WORD de 4 à 6 pages assez classique et nous souhaiterions avoir un document plus dynamique, tout en restant sobre. Les informations clés doivent être rapides à identifier et accessibles à l’œil facilement.
La cible :
Directeurs Généraux, Directeurs des Ressources Humaines, Responsable Recrutement
Tous secteurs d’activité
Groupes internationaux, Entreprises/Industries nationales ou locales, PME/PMI
Couleurs, favoris et autres exigences :
Cf notre logo et site internet : www.travenor-exemple.fr, tons bleus et blancs principalement
Sobriété, Simplicité
Nous sommes ouverts à toute proposition créative de votre part.

```html
<!DOCTYPE html>
<html lang="fr">
<head>
<meta charset="utf-8">
<title>Compte-rendu candidat</title>
<link href="https://fonts.googleapis.com/css2?family=Raleway:wght@300;400;600&display=swap" rel="stylesheet">
<style>
:root{
  --blue:#4a8fb8;
  --blue-dark:#2e6f8a;
  --text:#5a5a5a;
  --text-light:#8a8a8a;
  --rule:#7fa9c6;
  --confidential:#9b2740;
  --confidential-soft:#e3b3bf;
  --deco:#a9c3cf;
  --bg:#ffffff;
}
*{margin:0;padding:0;box-sizing:border-box}
html,body{width:1200px;height:849px;overflow:hidden;background:var(--bg)}
body{font-family:"Raleway",Arial,sans-serif;color:var(--text);position:relative;font-weight:300}
.page{position:relative;width:1200px;height:849px;overflow:hidden}

.decor{position:absolute;left:820px;top:170px;width:360px;height:560px;border-radius:180px 180px 120px 120px;
  background:radial-gradient(circle at 50% 35%,rgba(169,195,207,.55),rgba(169,195,207,.25) 60%,rgba(169,195,207,0) 75%)}

.brand{position:absolute;left:64px;top:26px;display:flex;align-items:center;gap:10px}
.brand-dot{width:18px;height:18px;border-radius:50%;background:var(--blue)}
.brand-name{font-size:22px;color:var(--blue);font-weight:400}

.header-box{position:absolute;left:60px;top:0;width:380px;height:300px;
  border-right:1.5px dashed var(--rule);border-bottom:1.5px dashed var(--rule)}
.place-date{position:absolute;right:24px;top:166px;text-align:right;font-size:14px;line-height:20px;color:var(--text)}
.candidate{position:absolute;right:24px;top:238px;text-align:right}
.candidate-label{font-size:15px;letter-spacing:.5px;color:var(--text)}
.candidate-name{font-size:26px;color:var(--blue);letter-spacing:1px;line-height:32px}

.confidential{position:absolute;left:760px;top:44px;width:440px;height:56px;background:var(--confidential);padding:6px 0 0 66px}
.confidential-title{color:#fff;font-size:16px;letter-spacing:2px}
.confidential-note{color:var(--confidential-soft);font-size:15px;letter-spacing:1.5px}

.section-marker{position:absolute;left:0;top:336px;width:24px;height:36px;background:var(--blue-dark)}
.section-title{position:absolute;left:80px;top:340px;font-size:23px;letter-spacing:2px;color:var(--blue)}

.col-left{position:absolute;left:60px;top:330px;width:380px;height:370px;
  border-right:1.5px dashed var(--rule);border-bottom:1.5px dashed var(--rule);padding:64px 28px 0 20px}
.col-left p{font-size:15px;line-height:24.5px;text-align:justify}
.col-right{position:absolute;left:470px;top:384px;width:690px}
.col-right p{font-size:15px;line-height:24.5px;text-align:justify;margin-bottom:22px}
strong{font-weight:600;color:#444}

.footer{position:absolute;left:50px;top:776px;right:0;height:50px;display:flex;font-size:12.5px;line-height:17px;color:var(--text-light)}
.footer .cell{padding:0 20px;border-left:1px solid #cfd8de}
.footer .cell:first-child{border-left:none;padding-left:0;color:var(--blue)}
.badge{position:absolute;left:1000px;top:778px;width:64px;height:44px;background:#3e6e8f}
.page-number{position:absolute;left:1136px;top:780px;font-size:16px;color:var(--blue);font-weight:600}
</style>
</head>
<body>
<div class="page">
  <div class="decor" role="img" aria-label="Grande loupe décorative en filigrane"></div>

  <div class="header-box">
    <div class="place-date">Nancy,<br>Le 14 décembre 2016</div>
    <div class="candidate">
      <div class="candidate-label">CANDIDATURE DE</div>
      <div class="candidate-name">PAUL MERCIER</div>
    </div>
  </div>

  <div class="brand"><span class="brand-dot"></span><span class="brand-name">Travenor Conseil</span></div>

  <div class="confidential">
    <div class="confidential-title">CONFIDENTIEL</div>
    <div class="confidential-note">ne pas communiquer au candidat</div>
  </div>

  <div class="section-marker"></div>
  <div class="col-left">
    <p><strong>Et prima post Osdroenam quam, ut dictum est, ab hac</strong> descriptione discrevimus, Commagena, nunc Euphratensis, clementer adsurgit. Hierapoli, vetere Nino et Samosata civitatibus amplis inlustris.<br>Eo adducta re <strong>per Isauriam, rege Persarum bellis</strong> finitimis inligato repellenteque a conlimitiis suis ferocissimas gentes, quae mente quadam versabili hostiliter eum saepe.</p>
  </div>
  <h2 class="section-title">SITUATION</h2>

  <div class="col-right">
    <p>Incessant et in nos arma moventem aliquotiens iuvant. Nohodares quidam nomine e numero optimatum, incursare Mesopotamiam quotiens copia dederit ordinatus, <strong>explorabat nostra sollicite, si repperisset usquam locum vi subita perrupturus.</strong></p>
    <p>Metuentes igitur idem latrones Lycaoniam magna parte campestrem cum se inpares nostris fore congressione stataria documentis frequentibus scirent, tramitibus deviis petivere Pamphyliam diu quidem intactam sed timore populationum et caedium, milite per omnia diffuso propinqua, magnis undique praesidiis communitam.</p>
  </div>

  <div class="footer">
    <div class="cell">www.travenor-exemple.fr<br>contact@travenor-exemple.fr</div>
    <div class="cell">27, rue des Tilleuls<br>54000 Nancy • FRANCE</div>
    <div class="cell">Tél : +33.383.000.112<br>Fax : +33.383.000.113</div>
    <div class="cell">SARL au capital de 20 000€ - 812 640 507 000 18 RCS<br>Nancy • 70222 • NII FR 00 812 640 507</div>
  </div>
  <div class="badge"></div>
  <div class="page-number">3</div>
</div>
</body>
</html>
```